Briar Ridge Target Range Facebook Design Project

I want a Facebook design based on my attached logo. I would like it to be classy, colorful, unusual.

Font:
- Serpentine-Bold-Bold for "BRIAR RIDGE"
- BrowalliaUPC for "TARGET RANGE"

Colors (CMYK code):
- BLACK ....... 0; 0; 0; 100;
- ORANGE ... gradient from 0; 65; 97.5; 0 to 0; 39; 97.5; 0

```html
<!DOCTYPE html>
<html lang="en">
<head>
<meta charset="utf-8">
<title>Briar Ridge Target Range</title>
<link rel="stylesheet" href="https://fonts.googleapis.com/css2?family=Open+Sans:wght@400;600&family=Orbitron:wght@700;800&display=swap">
<style>
:root{
  --black:#000000;
  --ink:#1d1d1d;
  --orange:#f7941d;
  --orange-deep:#f15a24;
  --orange-light:#f9a11b;
  --mist:#ebebeb;
  --paper:#ffffff;
  --text:#5a5a5a;
  --footer:#332f2e;
  --footer-text:#d6d2cf;
}
*{margin:0;padding:0;box-sizing:border-box}
html,body{width:843px;height:1200px;overflow:hidden}
body{position:relative;background:var(--orange);font-family:"Open Sans",Arial,sans-serif;color:var(--text)}
.display{font-family:"Orbitron","Arial Black",sans-serif;font-weight:800}

.top-band{position:absolute;left:0;top:0;width:843px;height:470px;background:var(--mist)}

.nav{position:absolute;left:0;top:0;width:843px;height:71px;background:var(--black);display:flex}
.nav a{display:block;height:71px;line-height:71px;color:#f2f2f2;text-decoration:none;font-size:17px;font-weight:600;letter-spacing:.3px;position:absolute;top:0}
.nav .is-active{background:linear-gradient(90deg,var(--orange-deep),var(--orange-light));color:var(--black);width:102px;left:0;padding-left:25px}
.nav .about{left:127px}
.nav .sports{left:265px}
.nav .contact{left:423px}

.brand{position:absolute;left:623px;top:12px;width:178px;height:176px;display:flex;flex-direction:column;align-items:center;justify-content:center;z-index:3}
.brand .dot{width:60px;height:60px;border-radius:50%;background:var(--orange);margin-bottom:10px}
.brand .name{font-family:"Orbitron","Arial Black",sans-serif;font-weight:800;font-size:16px;line-height:20px;color:var(--black);text-align:center}

.hero{position:absolute;left:23px;top:93px;width:797px;height:376px;background:var(--paper);box-shadow:0 22px 22px -16px rgba(0,0,0,.55)}
.hero-photo{position:absolute;left:0;top:0;width:405px;height:376px;background:radial-gradient(circle at 58% 45%,#ffffff 0,#f4f4f4 40%,#e2e2e2 70%,#cfc6bf 100%)}
.hero-title{position:absolute;left:420px;top:146px;font-size:21px;color:var(--orange-deep);letter-spacing:.5px}
.hero-text{position:absolute;left:420px;top:186px;width:352px;font-size:13.4px;line-height:23.5px;text-align:justify}

.welcome{position:absolute;left:23px;top:511px;width:797px;height:147px;background:var(--mist);text-align:center;box-shadow:0 22px 22px -16px rgba(0,0,0,.5)}
.welcome h1{margin-top:18px;font-size:20px;color:var(--ink);letter-spacing:.5px}
.welcome h1 span{color:var(--orange)}
.welcome p{margin:9px auto 0;width:740px;font-size:14.4px;line-height:23px}

.feature{position:absolute;top:696px;width:246px;height:297px;background:var(--paper);padding:5px}
.feature .photo{width:100%;height:100%}
.f1{left:23px}.f2{left:292px}.f3{left:561px}
.f1 .photo{background:linear-gradient(180deg,#dde3ea 0%,#cdd6de 50%,#8d8a85 80%,#5f7a3e 100%)}
.f2 .photo{background:linear-gradient(180deg,#4a5a45 0%,#e9e6e6 35%,#c94b4b 65%,#d77f85 85%,#eeeeee 100%)}
.f3 .photo{background:linear-gradient(180deg,#6a7a3a 0%,#8a9455 40%,#6a5443 70%,#4d7a32 100%)}
.badge{position:absolute;right:-12px;top:-14px;width:78px;height:78px;border-radius:50%;background:var(--paper);padding:5px}
.badge span{display:flex;width:100%;height:100%;border-radius:50%;border:3px solid var(--orange);background:radial-gradient(circle at 50% 30%,#555 0,#222 55%,#000 100%);align-items:center;justify-content:center;color:#fff;font-family:"Orbitron","Arial Black",sans-serif;font-weight:800;font-size:30px}

.footer{position:absolute;left:0;top:1022px;width:843px;height:178px;background:var(--footer)}
.footer h2{position:absolute;top:22px;font-size:15px;color:var(--orange);letter-spacing:.6px}
.footer ul{position:absolute;top:52px;list-style:none}
.footer li{font-size:13.4px;line-height:29px;color:var(--footer-text)}
.col-company h2,.col-company{left:0}
.h-company{left:22px}.l-company{left:27px}
.h-links{left:177px}.l-links{left:182px}
.h-contact{left:423px}
.contact-item{position:absolute;left:425px;display:flex;align-items:flex-start;font-size:13.4px;line-height:23px;color:var(--footer-text)}
.contact-item svg{flex:none;margin-right:12px;margin-top:4px}
.c-addr{top:50px}.c-phone{top:108px}.c-mail{top:137px}
.foot-brand{position:absolute;left:664px;top:18px;width:112px;display:flex;flex-direction:column;align-items:center}
.foot-brand .dot{width:40px;height:40px;border-radius:50%;background:var(--orange);margin-bottom:8px}
.foot-brand .name{font-family:"Orbitron","Arial Black",sans-serif;font-weight:800;font-size:11px;line-height:14px;color:var(--orange);text-align:center}
.copyright{position:absolute;left:636px;top:130px;font-size:13.4px;color:var(--footer-text)}
</style>
</head>
<body>
<div class="top-band"></div>

<nav class="nav">
  <a class="is-active" href="#">HOME</a>
  <a class="about" href="#">ABOUT US</a>
  <a class="sports" href="#">OUR SPORTS</a>
  <a class="contact" href="#">CONTACT</a>
</nav>

<section class="hero">
  <div class="hero-photo" role="img" aria-label="Hand holding a pistol aimed at a black and white ring target"></div>
  <h2 class="hero-title display">Lorem Ipsum Dolor Sit</h2>
  <p class="hero-text">Lorem ipsum dolor sit amet, consectetur adipiscing elit. Donec id tellus et erat aliquet sodales quis cursus nisi. Morbi scelerisque placerat sollicitudin.</p>
</section>

<div class="brand">
  <div class="dot"></div>
  <div class="name">BRIAR RIDGE<br>TARGET RANGE</div>
</div>

<section class="welcome">
  <h1 class="display"><span>Welcome to</span> Briar Ridge Target Range</h1>
  <p>Lorem ipsum dolor sit amet, consectetur adipiscing elit. Donec id tellus et erat aliquet sodales quis cursus nisi. Morbi scelerisque placerat sollicitudin. Nullam vulputate lorem a tempor blandit. Phasellus blandit dui eget nisl porttitor varius. Morbi eget consectetur diam. Quisque non est ligula.</p>
</section>

<article class="feature f1">
  <div class="photo" role="img" aria-label="Man aiming a scoped rifle outdoors"></div>
  <div class="badge"><span>1</span></div>
</article>
<article class="feature f2">
  <div class="photo" role="img" aria-label="Biathlete aiming a rifle at a snowy shooting range with numbered lanes"></div>
  <div class="badge"><span>2</span></div>
</article>
<article class="feature f3">
  <div class="photo" role="img" aria-label="Shooter with ear protection firing a shotgun beside an instructor"></div>
  <div class="badge"><span>3</span></div>
</article>

<footer class="footer">
  <h2 class="display h-company">COMPANY</h2>
  <ul class="l-company">
    <li>About</li><li>Players</li><li>Games</li><li>Support</li>
  </ul>
  <h2 class="display h-links">IMPORTANT LINKS</h2>
  <ul class="l-links">
    <li>Our Sports</li><li>Rules and Regulations</li><li>Contact</li><li>Complaints</li>
  </ul>
  <h2 class="display h-contact">CONTACT INFO</h2>
  <div class="contact-item c-addr">
    <svg width="12" height="18" viewBox="0 0 12 18"><path d="M6 0C2.7 0 0 2.6 0 5.9 0 10 6 18 6 18s6-8 6-12.1C12 2.6 9.3 0 6 0z" fill="#e98a23"/><circle cx="6" cy="6" r="2.3" fill="#332f2e"/></svg>
    <span>4215 Hollow Oak Lane,<br>Marrowfield, TN 38010.</span>
  </div>
  <div class="contact-item c-phone">
    <svg width="16" height="16" viewBox="0 0 16 16"><path d="M3.5 0.8l2.4 2.9-1.4 2c.9 2 2.6 3.7 4.6 4.6l2-1.4 2.9 2.4-1.6 2.6C6.6 13.6 2.4 9.4 0.9 3.6z" fill="#e98a23"/></svg>
    <span>+1 800 555 0147</span>
  </div>
  <div class="contact-item c-mail">
    <svg width="18" height="13" viewBox="0 0 18 13"><rect width="18" height="13" rx="1" fill="#e98a23"/><path d="M1 1.5l8 6 8-6" fill="none" stroke="#332f2e" stroke-width="1.4"/></svg>
    <span>info@briarridgerange.com</span>
  </div>
  <div class="foot-brand">
    <div class="dot"></div>
    <div class="name">BRIAR RIDGE<br>TARGET RANGE</div>
  </div>
  <p class="copyright">© 2014 | PRIVACY POLICY</p>
</footer>
</body>
</html>
```